New Logo design and Business cards

We are changing our business name and require a new Logo and business card design. Our new name will be "Brindlewood Garden Design & Construction" with a focus on enhancing our clients lifestyle through correct landscape design and construction of the designed landscape. We are a full service design to construct business meaning we take care of all aspects of designing and creating your ideal outdoor spaces. To see our current work and get a feel for what we do you can go to www.tarvogardens.com.au. We do not wish to have a major change to the website only the name/logo should change with all current colours etc being used in the new logo and business card. For our Logo I want the logo to reflect who we now are, and what we do, however I want it to have minimal impact on the website with the aim to only need to change the Logo and not colours or text styles. With the business card I need there to be a strong link between the card and the website with colours and looks being similar. I would love to see an image of one of our projects to be included on the card even as a backdrop. I have included a photo that I think could be used in the background of the business card. I have attached a copy of our current business cards (so you with have all relevant information required on the new cards) though I do want a fresh look with strong links to our website. Please feel free to contact me if you have any questions or ideas.

Brindlewood Garden Design & Construction-Shaping your weekends.

```html
<!DOCTYPE html>
<html lang="en">
<head>
<meta charset="utf-8">
<title>Brindlewood Garden Design &amp; Construction – Business Cards</title>
<link rel="stylesheet" href="https://fonts.googleapis.com/css2?family=Questrial&display=swap">
<style>
  :root {
    --bg: #ececec;
    --orchid: #c57bb7;
    --ink: #0b0b0b;
    --salmon: #f08a6c;
    --white: #ffffff;
    --lilac: #d69ad0;
    --photo-dark: #2a1a14;
    --photo-warm: #8a5a3a;
    --photo-green: #2f3a22;
  }
  * { margin: 0; padding: 0; box-sizing: border-box; }
  html, body { width: 1200px; height: 1000px; overflow: hidden; }
  body {
    background: var(--bg);
    font-family: "Questrial", "Century Gothic", sans-serif;
    color: var(--white);
    position: relative;
  }
  .card {
    position: absolute;
    width: 520px;
    height: 318px;
    overflow: hidden;
    box-shadow: 0 6px 18px rgba(0,0,0,0.18);
  }

  /* Back: contact card */
  .card--contact { left: 50px; top: 340px; background: var(--orchid); }
  .contact__brand {
    position: absolute; left: 30px; top: 28px;
    display: flex; align-items: center; gap: 10px;
  }
  .brand__dot {
    width: 26px; height: 26px; border-radius: 50%;
    background: var(--white); flex: none;
  }
  .brand__name { font-size: 15px; line-height: 1.2; letter-spacing: 0.3px; }
  .contact__person {
    position: absolute; right: 30px; top: 40px; text-align: right;
  }
  .person__name { font-size: 19px; font-weight: 700; letter-spacing: 0.5px; text-transform: uppercase; }
  .person__role { font-size: 13px; margin-top: 2px; }
  .contact__lines {
    position: absolute; right: 30px; top: 110px; text-align: right;
    font-size: 15px; line-height: 1.45;
  }
  .contact__lines b { font-weight: 700; }
  .contact__web { margin-top: 4px; }
  .contact__services {
    position: absolute; left: 0; right: 0; bottom: 12px; height: 62px;
    background: var(--ink); padding: 12px 30px 0;
    font-size: 13px; line-height: 1.45; color: #e8e8e8;
  }
  .contact__strip {
    position: absolute; left: 0; right: 0; bottom: 0; height: 12px;
    background: var(--salmon);
  }

  /* Front: photo card */
  .card--feature { left: 630px; top: 340px; background: var(--ink); }
  .feature__photo {
    position: absolute; left: 0; top: 0; width: 520px; height: 250px;
    background:
      radial-gradient(ellipse at 70% 60%, rgba(230,150,90,0.55), transparent 55%),
      linear-gradient(120deg, var(--photo-warm) 0%, var(--photo-dark) 45%, var(--photo-green) 100%);
  }
  .feature__brand {
    position: absolute; right: 40px; top: 110px;
    display: flex; align-items: center; gap: 12px;
  }
  .feature__brand .brand__dot { width: 34px; height: 34px; }
  .feature__brand .brand__name { font-size: 19px; }
  .feature__band {
    position: absolute; left: 0; right: 0; bottom: 0; height: 68px;
    background: var(--ink);
    display: flex; align-items: center; padding-left: 30px;
    font-size: 20px; letter-spacing: 0.3px;
  }
  .tag--lilac { color: var(--lilac); }
  .tag--salmon { color: var(--salmon); }
</style>
</head>
<body>

  <section class="card card--contact">
    <div class="contact__brand">
      <span class="brand__dot"></span>
      <span class="brand__name">Brindlewood<br>Garden Design &amp; Construction</span>
    </div>
    <div class="contact__person">
      <div class="person__name">Mara Quill</div>
      <div class="person__role">Director</div>
    </div>
    <div class="contact__lines">
      <div><b>P:</b> 04 2718 3946</div>
      <div><b>F:</b> 07 3190 2257</div>
      <div><b>E:</b> mara@tarvogardens.com.au</div>
      <div class="contact__web">www.tarvogardens.com.au</div>
    </div>
    <div class="contact__services">
      <div>CAD Design incl. 3D • Structural Landscaping</div>
      <div>Outdoor rooms, decks, gazebos • Excavation</div>
    </div>
    <div class="contact__strip"></div>
  </section>

  <section class="card card--feature">
    <div class="feature__photo" role="img" aria-label="Evening photograph of a landscaped courtyard with lit timber pergola, outdoor furniture and garden wall"></div>
    <div class="feature__brand">
      <span class="brand__dot"></span>
      <span class="brand__name">Brindlewood<br>Garden Design &amp; Construction</span>
    </div>
    <div class="feature__band">
      <span class="tag--lilac">Shaping</span>&nbsp;<span>your</span>&nbsp;<span class="tag--salmon">weekends</span>
    </div>
  </section>

</body>
</html>
```